Lumo - Booking activities for Kids and Adults.

The app allows booking of Kid's activities for a given date/time.
The app lists activities offered via various clubs (vendors) which a user can book for their kids.
The users can browse various clubs and their offered activities. The users can manage their kid's profiles.
Need a whole new look to the app. The existing app can be checked out at
https://apps.storefrontx.example/details?id=com.lumokw
https://appmarket.example/us/app/lumo-لومو/id9827315064?ls=1
Try using the app as Guest.

Target Market(s)

Kuwait

Font styles to use
Serif
Sans Serif

Requirements
Must have
• Home Screens
The home page should have everything from the existing app and a quick area to change between different kid's profile to see activities matching their interests ONLY. In the current version, there's no switch profile and hence we are showing the name tags on the activities.

We are also going to build ecommerce so we need that ecommerce look and feel.
Kindly maintain the image aspect ratio from the current app so the new version doesn't require new images.

Need a complete new innovative designs - Keep the color scheme same.
The designs should be minimalistic and image oriented. The design should be done in XD. The designs should be submitted in both light and dark theme.
Reference to be used - http://trevlan.example.uk

D.M for more info if needed.

```html
<!DOCTYPE html>
<html lang="en">
<head>
<meta charset="utf-8">
<title>Lumo – Schedule (Dark)</title>
<link href="https://fonts.googleapis.com/css2?family=Poppins:wght@400;500;600;700&display=swap" rel="stylesheet">
<style>
  :root{
    --page:#ffffff;
    --screen:#1b1b1b;
    --ink-dim:#0b0b0b;
    --muted-dim:#141414;
    --accent:#f9a83e;
    --accent-deep:#f39a2a;
    --pill-selected:#1f1306;
    --puzzles:#200f10;
    --tyedye:#0f1521;
    --green:#0b1c11;
    --nav:#363636;
    --nav-icon:#8c8c8c;
    --white:#ffffff;
  }
  *{box-sizing:border-box;margin:0;padding:0}
  html,body{width:1200px;height:1200px;overflow:hidden;background:var(--page);font-family:'Poppins',sans-serif}
  .screen{position:absolute;left:362px;top:85px;width:476px;height:1030px;background:var(--screen);
    box-shadow:0 10px 50px rgba(0,0,0,.35);overflow:hidden}
  .abs{position:absolute}
  .center{transform:translate(-50%,-50%);white-space:nowrap}
  .title{left:238px;top:101px;font-size:21px;font-weight:700;color:var(--ink-dim);letter-spacing:.5px}
  .avatar{left:384px;top:55px;width:52px;height:52px;border-radius:50%;
    background:radial-gradient(circle at 45% 40%,#3a2410,#24180c)}
  .month{top:224px;font-size:22px;font-weight:500;color:var(--muted-dim)}
  .month.current{color:var(--ink-dim);font-weight:600}
  .day-pill{top:264px;width:76px;height:140px;border-radius:38px;background:var(--pill-selected);left:200px}
  .day-num{top:324px;font-size:22px;font-weight:600;color:#161616}
  .day-name{top:352px;font-size:16px;font-weight:500;color:#161616}
  .day-num.sel,.day-name.sel{color:#3a250c}
  .time{font-size:18px;color:var(--ink-dim)}
  .card{left:166px;width:251px;height:88px;border-radius:44px}
  .card-title{left:35px;top:18px;font-size:19px;font-weight:600;color:rgba(255,255,255,.06)}
  .card-time{left:35px;top:52px;font-size:14px;color:rgba(255,255,255,.06)}
  .status{left:240px;top:622px;font-size:14px;color:#222}
  .label{font-size:14px;color:var(--white);font-weight:500}
  .label.accent{color:var(--accent);font-weight:700}
  .fab{border-radius:50%;background:var(--accent);display:flex;align-items:center;justify-content:center}
  .nav{left:0;top:945px;width:476px;height:85px;background:var(--nav);border-radius:37px 37px 0 0}
</style>
</head>
<body>
<main class="screen">
  <svg class="abs" style="left:54px;top:68px" width="24" height="26" viewBox="0 0 24 26"><path d="M16 3 L7 13 L16 23" fill="none" stroke="#0b0b0b" stroke-width="3.5" stroke-linecap="round" stroke-linejoin="round"/></svg>
  <h1 class="abs center title">SCHEDULE</h1>
  <div class="abs avatar" role="img" aria-label="Kid profile avatar illustration"></div>

  <span class="abs center month" style="left:66px">August</span>
  <span class="abs center month current" style="left:238px">September</span>
  <span class="abs center month" style="left:404px">October</span>

  <div class="abs day-pill"></div>
  <span class="abs center day-num" style="left:17px">10</span><span class="abs center day-name" style="left:17px">Sun</span>
  <span class="abs center day-num" style="left:128px">11</span><span class="abs center day-name" style="left:128px">Mon</span>
  <span class="abs center day-num sel" style="left:238px">12</span><span class="abs center day-name sel" style="left:238px">Tue</span>
  <span class="abs center day-num" style="left:345px">13</span><span class="abs center day-name" style="left:345px">Wed</span>
  <span class="abs center day-num" style="left:456px">14</span><span class="abs center day-name" style="left:456px">Thu</span>

  <span class="abs center time" style="left:86px;top:541px">10.00 AM</span>
  <span class="abs center time" style="left:86px;top:728px">01.00 PM</span>
  <span class="abs center time" style="left:86px;top:840px">03.00 PM</span>

  <div class="abs card" style="top:497px;background:var(--puzzles)">
    <span class="abs card-title">Puzzles</span><span class="abs card-time">10.00 am - 00.00 pm</span>
  </div>
  <svg class="abs" style="left:160px;top:599px" width="262" height="12"><line x1="6" y1="6" x2="256" y2="6" stroke="#1d0f10" stroke-width="2"/><circle cx="6" cy="6" r="6" fill="#230c0e"/><circle cx="132" cy="6" r="6" fill="#230c0e"/><circle cx="250" cy="6" r="6" fill="#230c0e"/></svg>
  <svg class="abs" style="left:209px;top:622px" width="18" height="20" viewBox="0 0 18 20"><circle cx="11" cy="3" r="2" fill="#222"/><path d="M6 19 L9 12 L12 14 L12 19 M9 12 L10 7 L14 10 M10 7 L5 9" fill="none" stroke="#222" stroke-width="1.6" stroke-linecap="round"/></svg>
  <span class="abs status">Starting, 2 hours left</span>

  <div class="abs card" style="top:684px;background:var(--tyedye)">
    <span class="abs card-title">Tye Dye</span><span class="abs card-time">01.00 pm - 03.00 pm</span>
  </div>
  <div class="abs card" style="top:797px;background:var(--green)">
    <span class="abs card-title">Painting</span><span class="abs card-time">03.00 pm - 04.00 pm</span>
  </div>

  <span class="abs center label accent" style="left:238px;top:747px">Switch Profile</span>
  <div class="abs fab" style="left:190px;top:780px;width:96px;height:96px;box-shadow:0 0 30px rgba(249,168,62,.5)">
    <svg width="64" height="64" viewBox="0 0 64 64"><circle cx="32" cy="32" r="28" fill="none" stroke="#0b0b0b" stroke-width="5"/><circle cx="32" cy="25" r="9" fill="none" stroke="#0b0b0b" stroke-width="5"/><path d="M14 51 C18 40 46 40 50 51" fill="none" stroke="#0b0b0b" stroke-width="5"/></svg>
  </div>

  <span class="abs center label" style="left:76px;top:830px">Add New Task</span>
  <div class="abs fab" style="left:93px;top:855px;width:62px;height:62px">
    <svg width="30" height="34" viewBox="0 0 30 34"><path d="M4 3 H19 L26 10 V31 H4 Z" fill="none" stroke="#0b0b0b" stroke-width="3" stroke-linejoin="round"/><path d="M15 14 V26 M9 20 H21" stroke="#0b0b0b" stroke-width="3"/></svg>
  </div>

  <span class="abs center label" style="left:399px;top:830px">Online Class</span>
  <div class="abs fab" style="left:322px;top:855px;width:62px;height:62px">
    <svg width="34" height="24" viewBox="0 0 34 24"><rect x="2" y="3" width="21" height="18" rx="3" fill="none" stroke="#0b0b0b" stroke-width="3"/><path d="M23 10 L32 5 V19 L23 14 Z" fill="#0b0b0b"/></svg>
  </div>

  <nav class="abs nav"></nav>
  <div class="abs" style="left:190px;top:897px;width:96px;height:96px;border-radius:50%;background:#170f05"></div>
  <div class="abs fab" style="left:203px;top:910px;width:70px;height:70px;background:linear-gradient(180deg,var(--accent),var(--accent-deep));box-shadow:0 0 24px rgba(249,168,62,.45)">
    <svg width="30" height="30" viewBox="0 0 30 30"><path d="M15 3 V27 M3 15 H27" stroke="#fff" stroke-width="5"/></svg>
  </div>

  <svg class="abs" style="left:34px;top:965px" width="44" height="44" viewBox="0 0 44 44"><path d="M4 22 L22 5 L40 22 M10 17 V40 H18 V28 H26 V40 H34 V17" fill="none" stroke="var(--nav-icon)" stroke-width="3.5" stroke-linejoin="round"/></svg>
  <svg class="abs" style="left:111px;top:965px" width="44" height="44" viewBox="0 0 44 44"><circle cx="22" cy="22" r="19" fill="none" stroke="var(--nav-icon)" stroke-width="3.5"/><path d="M30 14 L25 25 L14 30 L19 19 Z" fill="none" stroke="var(--nav-icon)" stroke-width="3"/></svg>
  <svg class="abs" style="left:325px;top:965px" width="44" height="44" viewBox="0 0 44 44"><rect x="4" y="7" width="36" height="34" rx="3" fill="none" stroke="var(--nav-icon)" stroke-width="3.5"/><path d="M4 14 H40" stroke="var(--nav-icon)" stroke-width="6"/><path d="M13 3 V9 M31 3 V9" stroke="var(--nav-icon)" stroke-width="3.5"/><rect x="11" y="24" width="4" height="4" fill="var(--nav-icon)"/><rect x="20" y="24" width="4" height="4" fill="var(--nav-icon)"/><rect x="29" y="24" width="4" height="4" fill="var(--nav-icon)"/></svg>
  <svg class="abs" style="left:400px;top:965px" width="44" height="44" viewBox="0 0 44 44"><circle cx="22" cy="22" r="19.5" fill="none" stroke="var(--nav-icon)" stroke-width="3.5"/><circle cx="22" cy="17" r="6" fill="none" stroke="var(--nav-icon)" stroke-width="3.5"/><path d="M10 35 C13 27 31 27 34 35" fill="none" stroke="var(--nav-icon)" stroke-width="3.5"/></svg>
</main>
</body>
</html>
```